Wholesale e-commerce website re-design

We are a wholesaler of African-made and African-themed products, and we're looking to update the look and feel of our website www.lomatrade.com to improve user experience. We'd like to have a cleaner homepage that keeps the product category menus (but simplifies them), allows certain products to be featured, and has a simple CTA box (something like "Login" for existing wholesale customers or "Start a Business" for new customers). The layout might be something along the lines of http://www.pinewellmarket.com/ except with a shopping cart featured at the top right. Our colors tend to be earth-toned, but the current color palate looks dated. Also see our blog.lomatrade.com page for themes and color ideas that are maybe more up-to-date. On our product pages, we want to feature the products more prominently and have simpler, cleaner Buy or Add buttons.

Other reference sites for inspiration: dravensupply.com, kettlorhome.com, http://www.pinewellmarket.com, http://morvanbulkgoods.com/ http://tenubra.com/
Updates

Project Deadline Extended
Reason: We like many of the designs that have been submitted so far, but need more time to make our final choice.

Target Market(s)

Small wholesale customers, most have a small business or home-based business. Also some retail, so an option for retail customers to click at the top to see retail pricing would be nice

Industry/Entity Type

Wholesale

Number of Pages Required

3 page

Font styles to use
Sans Serif

Requirements
Must have
• Clean, clear design that highlights products and reduces friction to customer purchase. Should include one homepage, one product page, and one shopping cart page design. Works with all browser types and be mobile-friendly.
Nice to have
• Other color schemes that would look good with our logo (maybe different from colors chosen below).
Should not have
• Splash pages with special effects, Adobe flash, elements that slow down page load times or that only work well in certain browsers.

```html
<!DOCTYPE html>
<html lang="en">
<head>
<meta charset="utf-8">
<title>Loma Trade — Wholesale African Goods</title>
<link href="https://fonts.googleapis.com/css2?family=Montserrat:wght@400;600;700&family=Open+Sans:wght@400;600;700&display=swap" rel="stylesheet">
<style>
:root{
  --red:#c8372b;
  --orange:#f5a31a;
  --ink:#222;
  --text:#555;
  --muted:#999;
  --topbar:#4d4d4d;
  --band:#5a5a5a;
  --footer:#eeeeee;
  --line:#e3e3e3;
  --white:#fff;
}
*{box-sizing:border-box;margin:0;padding:0}
html,body{width:1200px;height:3742px;overflow:hidden;background:var(--white)}
body{position:relative;font-family:'Open Sans',Arial,sans-serif;color:var(--text);font-size:13px}
.abs{position:absolute}
a{color:inherit;text-decoration:none}

.topbar{top:0;left:0;width:1200px;height:30px;background:var(--topbar);color:var(--white);font-size:11px}
.topbar ul{list-style:none;display:flex;gap:30px;position:absolute;right:100px;top:8px}
.topbar li{display:flex;align-items:center;gap:6px}
.topbar svg{width:12px;height:12px;fill:#fff}

.header{top:30px;left:0;width:1200px;height:95px}
.brand{position:absolute;left:100px;top:30px;display:flex;align-items:center;gap:10px;font-family:'Montserrat',sans-serif;font-weight:700;font-size:22px;color:var(--ink)}
.brand .dot{width:22px;height:22px;border-radius:50%;background:var(--red)}
.retail{position:absolute;left:332px;top:32px;font-size:11px;line-height:13px}
.retail b{color:var(--red);display:block;font-weight:600}
.retail span{color:var(--ink);font-weight:600}
.hlink{position:absolute;top:40px;font-size:12px;font-weight:600;color:var(--ink);display:flex;align-items:center;gap:7px}
.hlink svg{width:14px;height:14px;fill:var(--ink)}
.search{position:absolute;left:911px;top:40px;width:157px;height:30px;background:#ececec}
.search-btn{position:absolute;left:1068px;top:40px;width:32px;height:30px;background:var(--red);display:flex;align-items:center;justify-content:center}

.nav{top:125px;left:0;width:1200px;height:43px;background:var(--red)}
.nav ul{list-style:none;display:flex;justify-content:space-between;position:absolute;left:100px;width:1000px;top:0;height:43px;align-items:center}
.nav li{font-size:11px;font-weight:700;color:var(--white);padding:13px 6px}
.nav li.active{background:#2b2b2b}

.hero{top:168px;left:0;width:1200px;height:486px;background:linear-gradient(90deg,#d9d9d9,#f2f2f2 55%,#e6e6e6)}
.hero-photo{position:absolute;left:100px;top:30px;width:470px;height:456px;background:linear-gradient(180deg,#dcdcdc 0%,#cfd3df 30%,#4d5f9c 62%,#e7e9f0 100%)}
.hero-box{position:absolute;left:654px;top:169px;width:419px;height:199px;border:2px solid #333;text-align:center;padding-top:34px}
.hero-box h1{font-family:'Montserrat',sans-serif;font-weight:600;font-size:38px;color:var(--ink);letter-spacing:.5px}
.hero-box p{font-size:19px;color:#444;margin-top:6px;line-height:24px}
.hero-box .cta{display:block;color:var(--red);font-weight:700;font-size:20px;margin-top:18px}
.circle-arrow{position:absolute;width:28px;height:28px;border-radius:50%;background:#555;display:flex;align-items:center;justify-content:center}
.circle-arrow svg{width:12px;height:12px;stroke:#fff;fill:none;stroke-width:2.5}

.business{top:721px;left:100px;width:1000px;height:342px;border:1px solid var(--line)}
.business-photo{position:absolute;left:0;top:0;width:668px;height:340px;background:linear-gradient(180deg,#f6f4ef 0%,#e7dcc8 45%,#c9ae80 75%,#e9e2d4 100%)}
.business-copy{position:absolute;left:668px;top:0;width:330px;height:340px;text-align:center;padding-top:30px}
.business-copy h2{font-family:'Montserrat',sans-serif;font-size:23px;font-weight:600;color:var(--ink);line-height:31px}
.business-copy .price{font-size:21px;font-weight:700;color:var(--ink);margin-top:20px}
.business-copy .note{font-size:11px;color:#444}
.business-copy .desc{font-size:12px;color:#444;line-height:19px;margin:16px 22px 0}
.btn-red{display:inline-block;background:var(--red);color:#fff;font-family:'Montserrat',sans-serif;font-weight:700;font-size:14px}
.business-copy .btn-red{margin-top:16px;padding:9px 24px}

.cat{position:absolute;overflow:hidden}
.cat .label{position:absolute;font-family:'Montserrat',sans-serif;font-size:17px;color:#fff;letter-spacing:.4px}
.cat .frame{position:absolute;inset:12px;border:1px solid rgba(255,255,255,.7)}
.arrow-plain{position:absolute;width:22px;height:40px}
.arrow-plain svg{width:22px;height:40px;stroke:#666;fill:none;stroke-width:2}

.heading{left:0;width:1200px;text-align:center;font-family:'Montserrat',sans-serif;font-weight:700;font-size:32px;color:var(--ink)}

.product{position:absolute;width:225px;height:302px;border:1px solid var(--line);background:#fff;text-align:center}
.product .img{height:195px;border-bottom:1px solid var(--line)}
.product h3{font-size:14px;font-weight:600;color:var(--ink);margin-top:14px}
.product .price{font-size:11px;color:var(--red);margin-top:4px}
.product .actions{position:absolute;bottom:0;left:0;right:0;height:42px;border-top:1px solid var(--line);display:flex}
.product .actions span{flex:1;display:flex;align-items:center;justify-content:center;gap:6px;font-size:11px;color:#555}
.product .actions span+span{border-left:1px solid var(--line)}
.product .actions span.hot{background:var(--orange);color:#fff}
.product .actions svg{width:11px;height:11px;fill:currentColor}

.post{position:absolute;width:320px;height:334px}
.post .img{height:192px}
.post .date{position:absolute;left:0;top:0;width:46px;height:58px;background:#111;color:#fff;text-align:center;font-family:'Montserrat',sans-serif}
.post .date b{display:block;font-size:22px;padding-top:6px}
.post .date span{font-size:11px}
.post h3{font-size:18px;font-weight:600;color:var(--ink);margin-top:18px}
.post p{font-size:12px;color:var(--muted);line-height:17px;margin-top:6px}
.post .btn-red{position:absolute;left:0;bottom:0;width:130px;height:38px;line-height:38px;text-align:center;font-family:'Open Sans',sans-serif;font-weight:600;font-size:13px}

.feature{position:absolute;top:3169px;width:230px;text-align:center}
.feature svg{width:34px;height:30px;stroke:var(--red);fill:none;stroke-width:2}
.feature h4{font-family:'Montserrat',sans-serif;font-size:15px;font-weight:600;color:var(--ink);margin-top:6px}
.feature p{font-size:11px;color:var(--muted);font-style:italic;margin-top:2px}

.band{top:3331px;left:0;width:1200px;height:67px;background:var(--band);color:#fff}
.band .input{position:absolute;left:100px;top:18px;width:244px;height:32px;background:#fff;color:#999;font-size:11px;padding:9px 10px}
.band .sub{position:absolute;left:344px;top:18px;width:143px;height:32px;background:var(--red);text-align:center;line-height:32px;font-weight:700;font-size:13px}
.band .info{position:absolute;top:18px;display:flex;gap:12px;font-size:11px;line-height:15px}
.band .icon{width:30px;height:30px;border-radius:50%;background:var(--red);display:flex;align-items:center;justify-content:center;flex:none}
.band .icon svg{width:14px;height:14px;fill:#fff}
.band b{font-weight:700}

.footer{top:3398px;left:0;width:1200px;height:295px;background:var(--footer)}
.fcol{position:absolute;top:38px}
.fcol h5{font-family:'Montserrat',sans-serif;font-size:15px;font-weight:700;color:var(--ink);margin-bottom:12px;white-space:nowrap}
.fcol ul{list-style:none}
.fcol li{font-size:11px;color:#555;line-height:18px;padding-left:14px;position:relative;white-space:nowrap}
.fcol li::before{content:"";position:absolute;left:0;top:7px;width:5px;height:5px;border-radius:50%;background:var(--red)}
.fname{position:absolute;left:475px;top:60px;width:250px;text-align:center;font-family:'Montserrat',sans-serif;font-weight:700;font-size:38px;line-height:46px;color:#d6d6d6;letter-spacing:2px}
.social{position:absolute;left:494px;top:236px;display:flex;gap:12px}
.social i{width:22px;height:22px;border-radius:50%;border:1px solid #999;display:flex;align-items:center;justify-content:center}
.social i::after{content:"";width:6px;height:6px;border-radius:50%;background:#999}
.pay{position:absolute;left:861px;width:237px;height:62px;background:#fff;border:1px solid #ddd;padding:6px 8px}
.pay small{font-size:9px;color:#666;display:block}
.pay .cards{display:flex;gap:6px;margin-top:6px}
.pay .cards i{display:block;width:46px;height:26px;border-radius:3px}

.bottombar{top:3693px;left:0;width:1200px;height:49px;background:var(--topbar);color:#fff;font-size:12px}
.bottombar p{position:absolute;left:100px;top:16px}
</style>
</head>
<body>

<div class="abs topbar">
  <ul>
    <li><svg viewBox="0 0 12 12"><path d="M6 1 1 6h1.5v5h3V8h1v3h3V6H11z"/></svg></li>
    <li><svg viewBox="0 0 12 12"><rect x="1" y="1" width="10" height="10" rx="1"/></svg>Item Quick Order</li>
    <li><svg viewBox="0 0 12 12"><path d="M1 6 6 1h5v5l-5 5z"/></svg>Get Promotions</li>
    <li><svg viewBox="0 0 12 12"><circle cx="6" cy="4" r="3"/><path d="M1 12c0-3 2-5 5-5s5 2 5 5z"/></svg>Your Account</li>
    <li><svg viewBox="0 0 12 12"><path d="M1 2h10v8H1z"/></svg>Contact Us</li>
  </ul>
</div>

<header class="abs header">
  <div class="brand"><span class="dot"></span>Loma Trade</div>
  <div class="retail"><b>Retail Pricing</b><span>For Retail Customers</span></div>
  <a class="hlink" style="left:554px"><svg viewBox="0 0 14 14"><path d="M5 2 10 7 5 12V9H0V5h5z"/></svg>Sign In</a>
  <a class="hlink" style="left:649px"><svg viewBox="0 0 14 14"><path d="M2 10 9 3l2 2-7 7H2z"/></svg>Register</a>
  <a class="hlink" style="left:749px"><svg viewBox="0 0 14 14"><path d="M0 1h3l2 8h7l2-6H4"/><circle cx="6" cy="12" r="1.5"/><circle cx="11" cy="12" r="1.5"/></svg>Shopping Cart</a>
  <div class="search"></div>
  <div class="search-btn"><svg width="14" height="14" viewBox="0 0 14 14" fill="none" stroke="#fff" stroke-width="2"><circle cx="6" cy="6" r="4.5"/><path d="M9.5 9.5 13 13"/></svg></div>
</header>

<nav class="abs nav">
  <ul>
    <li class="active">African Clothing</li><li>African Fabrics</li><li>African Soaps</li><li>Oils, Incense &amp; Burners</li><li>Health &amp; Beauty</li><li>New Items</li><li>Jewelry</li><li>Musical Instruments</li><li>Artwork</li><li>All Categories</li>
  </ul>
</nav>

<section class="abs hero">
  <div class="hero-photo" role="img" aria-label="Two models wearing blue and white printed African tunics"></div>
  <div class="hero-box">
    <h1>AFRICAN CLOTHING</h1>
    <p>The largest selection of African<br>fashion anywhere</p>
    <a class="cta">Shop Now</a>
  </div>
  <div class="circle-arrow" style="left:41px;top:242px"><svg viewBox="0 0 12 12"><path d="M8 1 3 6l5 5"/></svg></div>
  <div class="circle-arrow" style="left:1129px;top:242px"><svg viewBox="0 0 12 12"><path d="M4 1l5 5-5 5"/></svg></div>
</section>

<section class="abs business">
  <div class="business-photo" role="img" aria-label="Business start-up kit of soaps, shea butter jars and oils"></div>
  <div class="business-copy">
    <h2>START YOUR AFRICAN<br>BUSINESS TODAY!</h2>
    <div class="price">Only $49.00 &amp; FREE Shipping</div>
    <div class="note">Free Shipping in the U.S. Only</div>
    <p class="desc">Get the Easy Business Start-Up Kit Today! Once you get the Start-Up Kit, you can immediately get new customers and start selling products.</p>
    <a class="btn-red">START A BUSINESS</a>
  </div>
</section>

<section class="abs" style="top:1150px;left:0;width:1200px;height:402px">
  <div class="arrow-plain" style="left:52px;top:181px"><svg viewBox="0 0 22 40"><path d="M20 1 2 20l18 19"/></svg></div>
  <div class="arrow-plain" style="left:1126px;top:181px"><svg viewBox="0 0 22 40"><path d="M2 1l18 19L2 39"/></svg></div>
  <div class="cat" style="left:100px;top:0;width:244px;height:402px;background:linear-gradient(180deg,#a7b9a8 0%,#b98a5c 45%,#c8632f 70%,#4f4a66 100%)" role="img" aria-label="Man in a colourful printed African shirt">
    <span class="label" style="left:14px;top:24px">AFRICAN CLOTHING</span></div>
  <div class="cat" style="left:357px;top:0;width:244px;height:402px;background:linear-gradient(180deg,#cfcfcf 0%,#6d6d6d 45%,#2e2a27 100%)" role="img" aria-label="Health and beauty bottles and jars">
    <div class="frame"></div><span class="label" style="left:0;width:244px;text-align:center;top:352px">HEALTH &amp; BEAUTY</span></div>
  <div class="cat" style="left:614px;top:0;width:282px;height:197px;background:linear-gradient(90deg,#a8342a 0%,#2f4f84 25%,#c9952e 50%,#7a2a22 75%,#3b6a43 100%)" role="img" aria-label="Folded printed African fabrics">
    <span class="label" style="left:0;width:282px;text-align:center;top:154px">AFRICAN FABRICS</span></div>
  <div class="cat" style="left:614px;top:210px;width:282px;height:192px;background:linear-gradient(180deg,#ececec 0%,#e3ddd6 45%,#8a5a36 75%,#d8d0c8 100%)" role="img" aria-label="Wooden hand drums">
    <div class="frame" style="border-color:#999"></div><span class="label" style="left:0;width:282px;text-align:center;top:26px;color:#333">MUSICAL INSTRUMENTS</span></div>
  <div class="cat" style="left:908px;top:0;width:192px;height:242px;background:linear-gradient(90deg,#ddd7cb 0%,#cfc6b4 45%,#5a3e2b 70%,#b98a3a 100%)" role="img" aria-label="Man wearing gold cuff bracelets">
    <span class="label" style="left:22px;top:52px;color:#333">JEWELRY</span></div>
  <div class="cat" style="left:908px;top:255px;width:192px;height:147px;background:linear-gradient(90deg,#efe7df 0%,#8a5a3a 50%,#efe7df 100%)" role="img" aria-label="Carved wooden masks">
    <div class="frame" style="border-color:#bbb"></div><span class="label" style="left:22px;top:58px;color:#333">ARTWORK</span></div>
</section>

<h2 class="abs heading" style="top:1697px">LATEST PRODUCTS</h2>

<section class="abs" style="top:1800px;left:0;width:1200px;height:640px">
  <div class="arrow-plain" style="left:45px;top:288px"><svg viewBox="0 0 22 40"><path d="M20 1 2 20l18 19"/></svg></div>
  <div class="arrow-plain" style="left:1133px;top:288px"><svg viewBox="0 0 22 40"><path d="M2 1l18 19L2 39"/></svg></div>

  <div class="product" style="left:112px;top:0">
    <div class="img" role="img" aria-label="Cowrie shell bracelet" style="background:linear-gradient(160deg,#f7f3ec,#e2d4bb)"></div>
    <h3>Cowrie Bracelet</h3><div class="price">Wholesale Price : $1.79 per ONE</div>
    <div class="actions"><span><svg viewBox="0 0 11 11"><path d="M1 8 7 2l2 2-6 6H1z"/></svg>Quick View</span><span><svg viewBox="0 0 11 11"><path d="M0 1h2l2 6h6l1-4H3"/></svg>Add To Cart</span></div>
  </div>
  <div class="product" style="left:362px;top:0">
    <div class="img" role="img" aria-label="Beaded leather bracelet" style="background:linear-gradient(160deg,#e9ebf1,#7e88a8)"></div>
    <h3>Leather Bracelet</h3><div class="price">Wholesale Price: $3.95 per ONE</div>
    <div class="actions"><span><svg viewBox="0 0 11 11"><path d="M1 8 7 2l2 2-6 6H1z"/></svg>Quick View</span><span><svg viewBox="0 0 11 11"><path d="M0 1h2l2 6h6l1-4H3"/></svg>Add To Cart</span></div>
  </div>
  <div class="product" style="left:611px;top:0">
    <div class="img" role="img" aria-label="Olive soap bar with box" style="background:linear-gradient(160deg,#eef3e2,#b6cc82)"></div>
    <h3>Anti-Aging Olive Soap</h3><div class="price">Wholesale Price: $1.99 per ONE</div>
    <div class="actions"><span><svg viewBox="0 0 11 11"><path d="M1 8 7 2l2 2-6 6H1z"/></svg>Quick View</span><span class="hot"><svg viewBox="0 0 11 11"><path d="M0 1h2l2 6h6l1-4H3"/></svg>Add To Cart</span></div>
  </div>
  <div class="product" style="left:861px;top:0">
    <div class="img" role="img" aria-label="Vetiver oil roller bottle" style="background:linear-gradient(160deg,#f4f8f7,#c6ddd8)"></div>
    <h3>Original Vetiver</h3><div class="price">Wholesale Price: $2.25 per ONE</div>
    <div class="actions"><span><svg viewBox="0 0 11 11"><path d="M1 8 7 2l2 2-6 6H1z"/></svg>Quick View</span><span><svg viewBox="0 0 11 11"><path d="M0 1h2l2 6h6l1-4H3"/></svg>Add To Cart</span></div>
  </div>

  <div class="product" style="left:112px;top:328px">
    <div class="img" role="img" aria-label="Set of painted African dolls" style="background:linear-gradient(160deg,#f4ebe6,#c47a63)"></div>
    <h3>African Doll</h3><div class="price">Wholesale Price: $4.95 per EACH</div>
    <div class="actions"><span><svg viewBox="0 0 11 11"><path d="M1 8 7 2l2 2-6 6H1z"/></svg>Quick View</span><span><svg viewBox="0 0 11 11"><path d="M0 1h2l2 6h6l1-4H3"/></svg>Add To Cart</span></div>
  </div>
  <div class="product" style="left:362px;top:328px">
    <div class="img" role="img" aria-label="Small wooden balafon" style="background:linear-gradient(160deg,#f1ebe4,#a98561)"></div>
    <h3>Balafon X-Small</h3><div class="price">Wholesale Price: $14.95 per ONE</div>
    <div class="actions"><span><svg viewBox="0 0 11 11"><path d="M1 8 7 2l2 2-6 6H1z"/></svg>Quick View</span><span><svg viewBox="0 0 11 11"><path d="M0 1h2l2 6h6l1-4H3"/></svg>Add To Cart</span></div>
  </div>
  <div class="product" style="left:611px;top:328px">
    <div class="img" role="img" aria-label="Red embroidered elephant handbag" style="background:linear-gradient(160deg,#f6e4e3,#cf4a44)"></div>
    <h3>Elephant Handbag</h3><div class="price">Wholesale Price: $5.95 per ONE</div>
    <div class="actions"><span><svg viewBox="0 0 11 11"><path d="M1 8 7 2l2 2-6 6H1z"/></svg>Quick View</span><span><svg viewBox="0 0 11 11"><path d="M0 1h2l2 6h6l1-4H3"/></svg>Add To Cart</span></div>
  </div>
  <div class="product" style="left:861px;top:328px">
    <div class="img" role="img" aria-label="Beaded necklace on a display stand" style="background:linear-gradient(160deg,#f7f4ef,#dcc29a)"></div>
    <h3>Maasai Beaded Necklace</h3><div class="price">Wholesale Price: $1.95 per ONE</div>
    <div class="actions"><span><svg viewBox="0 0 11 11"><path d="M1 8 7 2l2 2-6 6H1z"/></svg>Quick View</span><span><svg viewBox="0 0 11 11"><path d="M0 1h2l2 6h6l1-4H3"/></svg>Add To Cart</span></div>
  </div>
</section>

<a class="abs btn-red" style="top:2475px;left:535px;width:130px;height:38px;line-height:38px;text-align:center;font-family:'Open Sans',sans-serif;font-weight:600;font-size:13px">View All</a>

<h2 class="abs heading" style="top:2645px">LATEST BLOG POSTS</h2>

<article class="post" style="left:100px;top:2760px">
  <div class="img" role="img" aria-label="Drummers in white robes at a festival" style="background:linear-gradient(180deg,#c3d3e2 0%,#d8cdb8 45%,#8a6a48 100%)"></div>
  <div class="date"><b>10</b><span>Dec</span></div>
  <h3>Duis autem vel eum iriure</h3>
  <p>Ut wisi enim ad minim veniam, quis nostrud non exerci tation commodo consequat.</p>
  <a class="btn-red">Read More</a>
</article>
<article class="post" style="left:441px;top:2760px">
  <div class="img" role="img" aria-label="Group of women in colourful dresses" style="background:linear-gradient(90deg,#3a3a3a 0%,#a9542f 35%,#dcc7a6 65%,#3c3c3c 100%)"></div>
  <div class="date"><b>10</b><span>Dec</span></div>
  <h3>Duis autem vel eum iriure</h3>
  <p>Ut wisi enim ad minim veniam, quis nostrud non exerci tation commodo consequat.</p>
  <a class="btn-red">Read More</a>
</article>
<article class="post" style="left:781px;top:2760px">
  <div class="img" role="img" aria-label="Model in a blue printed outfit against the sky" style="background:linear-gradient(180deg,#3f8fd6 0%,#7fb6e8 50%,#2a3a6c 100%)"></div>
  <div class="date"><b>10</b><span>Dec</span></div>
  <h3>Duis autem vel eum iriure</h3>
  <p>Ut wisi enim ad minim veniam, quis nostrud non exerci tation commodo consequat.</p>
  <a class="btn-red">Read More</a>
</article>

<div class="feature" style="left:60px">
  <svg viewBox="0 0 34 30"><path d="M2 6h18v14H2zM20 11h7l5 5v4H20"/><circle cx="8" cy="23" r="3"/><circle cx="26" cy="23" r="3"/></svg>
  <h4>FREE DELIVERY</h4><p>24/7 Freeship</p></div>
<div class="feature" style="left:332px">
  <svg viewBox="0 0 34 30"><path d="M4 6h18l8 9-8 9H4z"/><circle cx="10" cy="15" r="2"/></svg>
  <h4>SALE &amp; DISCOUNT</h4><p>24/7 Freeship</p></div>
<div class="feature" style="left:604px">
  <svg viewBox="0 0 34 30"><rect x="4" y="3" width="26" height="18" rx="1"/><path d="M13 27h8M17 21v6"/></svg>
  <h4>EASY BUY ONLINE</h4><p>24/7 Freeship</p></div>
<div class="feature" style="left:888px">
  <svg viewBox="0 0 34 30"><path d="M5 9 17 3l12 6v13l-12 6-12-6zM5 9l12 6 12-6M17 15v13"/></svg>
  <h4>WHOLESALER</h4><p>24/7 Freeship</p></div>

<section class="abs band">
  <div class="input">Enter your email here</div>
  <div class="sub">Subscribe</div>
  <div class="info" style="left:499px"><span class="icon"><svg viewBox="0 0 14 14"><path d="M7 1a4 4 0 0 0-4 4c0 3 4 8 4 8s4-5 4-8a4 4 0 0 0-4-4zm0 5.5A1.5 1.5 0 1 1 7 3.5a1.5 1.5 0 0 1 0 3z"/></svg></span><span>118 Orchard Row, Suite B<br>Fairbrook, NJ 07999</span></div>
  <div class="info" style="left:753px"><span class="icon"><svg viewBox="0 0 14 14"><path d="M3 1h3l1 3-2 1.5a8 8 0 0 0 3.5 3.5L10 7l3 1v3c0 1-1 2-2 2A10 10 0 0 1 1 3c0-1 1-2 2-2z"/></svg></span><span><b>CALL US :</b><br>(555)014-2286</span></div>
  <div class="info" style="left:916px"><span class="icon"><svg viewBox="0 0 14 14"><path d="M1 3h12v8H1zM1 3l6 5 6-5" stroke="#c8372b" stroke-width="1"/></svg></span><span><b>EMAIL US :</b><br>contact@lomatrade.com</span></div>
</section>

<footer class="abs footer">
  <div class="fcol" style="left:100px"><h5>QUICK LINKS</h5><ul>
    <li>Home</li><li>Item Quick Order</li><li>Web Specials</li><li>Top 10 Bestsellers</li><li>Your Account</li><li>Shopping Cart</li><li>About Us</li><li>Contact Us</li></ul></div>
  <div class="fcol" style="left:268px"><h5>BUSINESS TOOLS</h5><ul>
    <li>Free Printable Products</li><li>Get Your Own African Website</li><li>Fast Start Up Kit</li><li>How to Start a New Business</li><li>Promotional Tools</li><li>Affiliate Program</li></ul></div>
  <div class="fname">LOMA<br>TRADE</div>
  <div class="social"><i></i><i></i><i></i><i></i></div>
  <div class="fcol" style="left:686px"><h5>CUSTOMER HELP</h5><ul>
    <li>Catalog (New December Flier)</li><li>African Stores Near You</li><li>Frequently Asked Questions</li><li>Shipping Policies</li><li>See Retail Pricing</li></ul></div>
  <div class="fcol" style="left:893px"><h5>ABOUT LOMA TRADE</h5><ul>
    <li>About Loma Trade</li><li>How We Help Africa</li><li>African Proverbs</li><li>Free Articles</li><li>How Can We Improve?</li></ul></div>
</footer>

<div class="abs bottombar"><p>Copyright © 2017 Loma Trade. All Right Reserved.</p></div>

<div class="pay" style="top:3668px">
  <small>We Accept</small>
  <div class="cards"><i style="background:#cfd8e6"></i><i style="background:#e3d2c8"></i><i style="background:#d6dbe6"></i><i style="background:#cfe0ea"></i></div>
</div>

</body>
</html>
```